Business Card for premium dental clinic

We are a premium dental clinic based in Brasov, Romania with more than 15 year on the market, providing quality dental treatment made by a team of more specialized dentists, working with modern equipment as a solution to beautiful and healthy teeth.

Our current logo for the clinic use 2 square with colors black and gold - dr Corbescu - studio, using family fonts Bodoni, Myriad Pro and Segoe Print.
Depending on the printing we used some gold CMYK background or gold foil picture background or a gold gradient.
We want a business card:
- eye catching business card
- distinguished business card
- premium design
- to keep the color scheme of black and gold
- to attract the customers to spent time reading the information
- modern concept

```html
<!DOCTYPE html>
<html lang="en">
<head>
<meta charset="utf-8">
<title>dr Corbescu – Business Card</title>
<link href="https://fonts.googleapis.com/css2?family=Poppins:wght@400;500;600&display=swap" rel="stylesheet">
<style>
  :root {
    --canvas: #e0e0e0;
    --card-dark: #1c1c1c;
    --card-deep: #111111;
    --gold-light: #f2dc5a;
    --gold: #d4a92a;
    --gold-deep: #9c7412;
    --ink: #1a1a1a;
    --paper: #ffffff;
    --text-light: #f4f4f4;
  }
  * { box-sizing: border-box; margin: 0; padding: 0; }
  html, body { width: 1200px; height: 1200px; overflow: hidden; }
  body {
    background: var(--canvas);
    font-family: "Poppins", sans-serif;
    position: relative;
  }
  .card {
    position: absolute;
    left: 231px;
    width: 738px;
    height: 421px;
    border-radius: 34px;
    background: radial-gradient(ellipse at 40% 40%, var(--card-dark), var(--card-deep));
    overflow: hidden;
  }
  .card--front { top: 129px; }
  .card--back { top: 648px; }

  .edge-tab {
    position: absolute;
    top: 112px;
    width: 16px;
    height: 197px;
    background: linear-gradient(90deg, var(--gold-deep), var(--gold-light) 55%, var(--gold));
  }
  .edge-tab--left { left: 0; border-radius: 0 4px 4px 0; }
  .edge-tab--right { right: 0; border-radius: 4px 0 0 4px; }

  .brand-block {
    position: absolute;
    display: flex;
  }
  .card--front .brand-block { left: 152px; top: 104px; width: 432px; height: 213px; }
  .card--back .brand-block { left: 0; top: 129px; width: 331px; height: 164px; }

  .gold-foil {
    flex: 1;
    background:
      radial-gradient(circle at 35% 30%, var(--gold-light), transparent 55%),
      radial-gradient(circle at 60% 85%, #e8c63e, transparent 50%),
      linear-gradient(135deg, var(--gold), var(--gold-deep));
  }
  .brand-panel {
    flex: 1;
    background: var(--paper);
    display: flex;
    align-items: center;
    justify-content: center;
    gap: 10px;
  }
  .brand-square {
    background: var(--ink);
    width: 16px;
    height: 16px;
  }
  .brand-name {
    font-weight: 500;
    color: var(--ink);
    white-space: nowrap;
  }
  .card--front .brand-name { font-size: 26px; }
  .card--back .brand-name { font-size: 19px; }
  .card--back .brand-square { width: 12px; height: 12px; }

  .contact {
    position: absolute;
    left: 366px;
    top: 78px;
    color: var(--text-light);
  }
  .contact__name { font-size: 24px; font-weight: 600; line-height: 1.1; }
  .contact__role { font-size: 21px; font-weight: 400; line-height: 1.4; }
  .contact__address { margin-top: 6px; font-size: 18px; line-height: 1.38; }
  .contact__list { list-style: none; margin-top: 18px; }
  .contact__item {
    display: flex;
    align-items: center;
    gap: 12px;
    font-size: 19.5px;
    height: 34.5px;
  }
  .contact__icon { width: 28px; height: 28px; flex: none; }
</style>
</head>
<body>
  <svg width="0" height="0" style="position:absolute">
    <defs>
      <linearGradient id="icon-gold" x1="0" y1="0" x2="1" y2="1">
        <stop offset="0" stop-color="#f2dc5a"/>
        <stop offset="0.6" stop-color="#d4a92a"/>
        <stop offset="1" stop-color="#8a6510"/>
      </linearGradient>
    </defs>
  </svg>

  <section class="card card--front" aria-label="Card front">
    <div class="edge-tab edge-tab--left"></div>
    <div class="edge-tab edge-tab--right"></div>
    <div class="brand-block">
      <div class="gold-foil" role="img" aria-label="Gold foil texture"></div>
      <div class="brand-panel">
        <span class="brand-square"></span>
        <span class="brand-name">dr Corbescu</span>
      </div>
    </div>
  </section>

  <section class="card card--back" aria-label="Card back">
    <div class="brand-block">
      <div class="gold-foil" role="img" aria-label="Gold foil texture"></div>
      <div class="brand-panel">
        <span class="brand-square"></span>
        <span class="brand-name">dr Corbescu</span>
      </div>
    </div>

    <div class="contact">
      <p class="contact__name">Name</p>
      <p class="contact__role">Director</p>
      <p class="contact__address">Your Address<br>Street Location City</p>
      <ul class="contact__list">
        <li class="contact__item">
          <svg class="contact__icon" viewBox="0 0 28 28" aria-hidden="true">
            <circle cx="14" cy="14" r="13.5" fill="url(#icon-gold)"/>
            <path d="M9 7.5c1-.6 1.8-.3 2.3.6l1.2 2.2c.4.8.2 1.5-.5 2l-.8.6c.7 1.6 1.8 2.8 3.4 3.6l.6-.8c.5-.7 1.3-.9 2-.5l2.2 1.3c.9.5 1.1 1.3.5 2.3-.9 1.5-2.6 1.9-4.2 1.1-3.4-1.7-5.9-4.3-7.5-7.7-.7-1.6-.3-3.3 1.8-4.7z" fill="#1a1a1a"/>
          </svg>
          <span>+1234567890</span>
        </li>
        <li class="contact__item">
          <svg class="contact__icon" viewBox="0 0 28 28" aria-hidden="true">
            <circle cx="14" cy="14" r="13.5" fill="url(#icon-gold)"/>
            <rect x="9.5" y="6" width="9" height="16" rx="1.6" fill="none" stroke="#1a1a1a" stroke-width="1.8"/>
            <circle cx="14" cy="19.3" r="1" fill="#1a1a1a"/>
          </svg>
          <span>+1234567890</span>
        </li>
        <li class="contact__item">
          <svg class="contact__icon" viewBox="0 0 28 28" aria-hidden="true">
            <circle cx="14" cy="14" r="13.5" fill="url(#icon-gold)"/>
            <rect x="6.5" y="9" width="15" height="10.5" fill="none" stroke="#1a1a1a" stroke-width="1.6"/>
            <path d="M6.8 9.3 14 15l7.2-5.7M6.8 19.2l5.3-4.8M21.2 19.2l-5.3-4.8" fill="none" stroke="#1a1a1a" stroke-width="1.4"/>
          </svg>
          <span>info@corbescudental.com</span>
        </li>
        <li class="contact__item">
          <svg class="contact__icon" viewBox="0 0 28 28" aria-hidden="true">
            <circle cx="14" cy="14" r="13.5" fill="url(#icon-gold)"/>
            <g fill="none" stroke="#1a1a1a" stroke-width="1.4">
              <circle cx="14" cy="14" r="8"/>
              <ellipse cx="14" cy="14" rx="3.5" ry="8"/>
              <path d="M6 14h16M7.2 10h13.6M7.2 18h13.6"/>
            </g>
          </svg>
          <span>www.corbescudental.com</span>
        </li>
      </ul>
    </div>
  </section>
</body>
</html>
```